Business Card design for Recruiter providing Recruitment Staff Augmentation services

I need a double sided business card. I have used Plix to print cards in the past and really like their quality. I have a logo but need to change the tagline that is part of the graphic.

The tagline currently reads and Connnecting people with careers - but it should be removed.

The back should look like a notecard for writing a to do list with the first to-do Augment Recruiting Staff

```html
<!DOCTYPE html>
<html lang="en">
<head>
<meta charset="utf-8">
<title>Talent Summit Business Card</title>
<link rel="stylesheet" href="https://fonts.googleapis.com/css2?family=Questrial&display=swap">
<style>
  :root {
    --page-bg: #e9e6e1;
    --card-white: #fbfbfa;
    --card-grey: #ececec;
    --navy: #0b4a6c;
    --accent-red: #d2492a;
    --ink-light: #ffffff;
    --rule: #1d4f6e;
  }
  * { box-sizing: border-box; margin: 0; padding: 0; }
  html, body {
    width: 1200px;
    height: 1023px;
    overflow: hidden;
    background: var(--page-bg);
    font-family: "Questrial", "Century Gothic", sans-serif;
  }
  .sheet { position: relative; width: 1200px; height: 1023px; }
  .card {
    position: absolute;
    left: 300px;
    width: 600px;
    height: 343px;
    overflow: hidden;
    box-shadow: 0 6px 18px rgba(0, 0, 0, 0.18);
  }
  .card--front { top: 110px; background: var(--card-white); }
  .card--back { top: 570px; background: var(--card-grey); }
  .card__art { position: absolute; inset: 0; }

  .brand {
    position: absolute;
    display: flex;
    align-items: center;
    gap: 12px;
    color: var(--navy);
    font-size: 28px;
    letter-spacing: 1px;
    white-space: nowrap;
  }
  .brand__dot { width: 28px; height: 28px; border-radius: 50%; background: var(--accent-red); }
  .card--front .brand { left: 34px; top: 150px; }
  .card--back .brand { left: 34px; top: 34px; }

  .contact {
    position: absolute;
    left: 282px;
    top: 212px;
    color: var(--ink-light);
    white-space: nowrap;
  }
  .contact__name { font-size: 19px; line-height: 24px; }
  .contact__role { font-size: 13px; line-height: 16px; margin-bottom: 12px; }
  .contact__line { display: flex; align-items: center; gap: 7px; font-size: 13px; line-height: 18px; }
  .contact__icon { width: 11px; height: 11px; flex: none; }

  .address {
    position: absolute;
    left: 440px;
    top: 150px;
    color: var(--ink-light);
    font-size: 13px;
    line-height: 18px;
    white-space: nowrap;
  }

  .todo-lines { position: absolute; left: 34px; right: 34px; top: 110px; }
  .todo-lines__rule { height: 0; border-top: 2px solid var(--rule); margin-bottom: 48px; }
</style>
</head>
<body>
<main class="sheet">

  <section class="card card--front" aria-label="Card front">
    <svg class="card__art" viewBox="0 0 600 343" aria-hidden="true">
      <path d="M0 300 Q 380 250 520 0 L 600 0 L 600 343 L 0 343 Z" fill="var(--navy)"/>
      <path d="M-10 287 Q 368 237 506 -10" fill="none" stroke="var(--accent-red)" stroke-width="8"/>
    </svg>

    <div class="brand">
      <span class="brand__dot"></span>
      <span class="brand__name">TALENT SUMMIT</span>
    </div>

    <div class="contact">
      <p class="contact__name">Dana Whitlow, SPHR</p>
      <p class="contact__role">Managing Director</p>
      <p class="contact__line">
        <svg class="contact__icon" viewBox="0 0 12 12" aria-hidden="true"><path d="M2 1 L4.5 1 L5.5 3.5 L4 4.7 C4.8 6.4 5.6 7.2 7.3 8 L8.5 6.5 L11 7.5 L11 10 C6 11 1 6 2 1 Z" fill="currentColor"/></svg>
        555-014-2290
      </p>
      <p class="contact__line">
        <svg class="contact__icon" viewBox="0 0 12 12" aria-hidden="true"><rect x="0.5" y="2" width="11" height="8" fill="currentColor"/><path d="M0.5 2 L6 6.5 L11.5 2" fill="none" stroke="var(--navy)" stroke-width="1"/></svg>
        Dana@talentsummit.com
      </p>
      <p class="contact__line">
        <svg class="contact__icon" viewBox="0 0 12 12" aria-hidden="true"><circle cx="6" cy="6" r="5.3" fill="currentColor"/><path d="M0.7 6 H11.3 M6 0.7 V11.3 M6 0.7 C3 4 3 8 6 11.3 M6 0.7 C9 4 9 8 6 11.3" fill="none" stroke="var(--navy)" stroke-width="0.8"/></svg>
        www.talentsummit.com
      </p>
    </div>

    <p class="address">Here your company or<br>home address</p>
  </section>

  <section class="card card--back" aria-label="Card back">
    <div class="brand">
      <span class="brand__dot"></span>
      <span class="brand__name">TALENT SUMMIT</span>
    </div>
    <div class="todo-lines">
      <div class="todo-lines__rule"></div>
      <div class="todo-lines__rule"></div>
      <div class="todo-lines__rule"></div>
      <div class="todo-lines__rule"></div>
    </div>
  </section>

</main>
</body>
</html>
```